Rack Card for Charter Sail Boat business in SF Bay

We are in need of a rack card design to highlight the business to tourists and locals. 2 sided card 3.86" x 8.39" (full bleed)

We are looking for visually appleaing designs on the front and back but a little more detail on the back.

Use the info provided (text and info) on the website to include the 3 key services (Quick, 1/2 day, fullday) and aspects of the boat, location and other key info for customers (not prices). DO NOT INCLUDE ALL THIS TEXT please pick the elements you would like to fit your design and inform the customer as you would like about the business.

I can also provide photos directly from the video if you think those would fit your design. If video doesn't work on this upload you can view it at the website or facebook page (www.fb.com/tidewrenllc)

Now included a few video pictures in files for your use

Target Market(s)

Tourists and locals to san francisco east bay. 25 - 55 years old. Men and women.

Industry/Entity Type

Entertainment

Colors
0455a3
ec1f27
f3f1f8

Requirements
Must have
• Highlight services, key contact information (email, phone, website site), Visual impact
• 2-sided card - 3.86" x 8.39" (98 x 213 mm)
Nice to have
• facebook link, electric engine(green),

```html
<!DOCTYPE html>
<html lang="en">
<head>
<meta charset="utf-8">
<title>Tidewren Sail – Rack Card</title>
<link href="https://fonts.googleapis.com/css2?family=Roboto+Slab:wght@300;400;800&display=swap" rel="stylesheet">
<style>
  :root{
    --blue:#0455a3;
    --blue-deep:#1d4f97;
    --blue-dark:#173f7c;
    --red:#ec1f27;
    --red-deep:#c8242b;
    --mist:#f3f1f8;
    --sky:#6fb8e8;
    --white:#ffffff;
    --ink:#3a3a3a;
    --page:#e9e7ee;
  }
  *{box-sizing:border-box;margin:0;padding:0}
  html,body{width:1200px;height:1000px;overflow:hidden}
  body{background:var(--page);font-family:"Roboto Slab",serif;position:relative}
  .card{position:absolute;top:40px;width:433px;height:920px;overflow:hidden;box-shadow:0 4px 14px rgba(0,0,0,.25)}
  .card--front{left:127px;background:var(--blue-deep)}
  .card--back{left:620px;background:var(--mist)}
  .abs{position:absolute}

  /* front */
  .front-photo-top{left:0;top:0;width:433px;height:300px;background:linear-gradient(160deg,#8fb3d6 0%,#cfd8e2 40%,#5b6f86 75%,#2b3b55 100%)}
  .front-photo-main{left:0;top:280px;width:433px;height:520px;background:linear-gradient(100deg,#1f56a4 0%,#2a5ea8 35%,#5d86b5 62%,#6f8fae 78%,#1c2c48 100%)}
  .front-shapes{left:0;top:0}
  .front-title{left:0;top:312px;width:433px;text-align:center;color:var(--white);font-weight:800;font-size:29px;line-height:34px;letter-spacing:.3px}
  .badge{left:40px;top:490px}
  .checklist{left:46px;top:618px;list-style:none;color:var(--white);font-weight:800;font-size:28px;line-height:43px}
  .checklist li{display:flex;align-items:center;gap:12px}
  .checklist svg{flex:none}
  .brand-seal{left:20px;top:770px;width:160px;height:160px;border-radius:50%;background:var(--white);border:4px solid var(--red);display:flex;align-items:center;justify-content:center;color:var(--blue);font-weight:400;font-size:26px}
  .front-contact{right:18px;top:833px;text-align:right;color:var(--blue-dark);font-size:13px;line-height:19px}
  .phone{display:flex;align-items:center;justify-content:flex-end;gap:5px;font-weight:800;font-size:16px;color:var(--blue-dark)}
  .socials{display:flex;gap:6px;justify-content:flex-end;margin-top:5px}
  .socials span{width:14px;height:14px;border-radius:2px;background:var(--blue)}

  /* back */
  .intro{left:0;top:0;width:433px;height:198px;background:var(--blue-deep);padding:22px 22px 0;color:var(--white)}
  .intro h2{text-align:center;font-weight:800;font-size:24px;letter-spacing:.5px;margin-bottom:8px}
  .intro p{font-weight:300;font-size:12.6px;line-height:17px;text-align:justify}
  .intro-rule{left:0;top:196px;width:433px;height:4px;background:var(--red)}
  .trip-bg{left:0;top:200px;width:433px;height:420px;background:linear-gradient(180deg,#e4e6eb 0%,#f1f1f4 45%,#dcdfe5 100%)}
  .trip-tab{left:128px;top:183px;width:177px;height:40px;background:var(--red-deep);border-radius:6px;color:var(--white);font-weight:800;font-size:25px;text-align:center;line-height:40px}
  .map{width:122px;height:122px;border-radius:50%;border:4px solid var(--blue-deep);box-shadow:0 0 0 3px var(--white);background:radial-gradient(circle at 45% 55%,#b7d6ee 0%,#a6cbe8 45%,#d9e4cf 70%,#e9ecdc 100%)}
  .trip h3{color:var(--blue-deep);font-weight:800;font-size:17px;line-height:20px;margin-bottom:3px}
  .trip p{color:var(--ink);font-weight:300;font-size:12.4px;line-height:16.5px}
  .trip--right{text-align:right}
  .gallery{left:0;top:620px;width:433px;height:145px;background:var(--sky)}
  .shot{top:15px;height:113px;border:3px solid var(--white);background:linear-gradient(160deg,#8fb6d8,#4d6480 55%,#6a5040)}
  .shot--deck{background:linear-gradient(180deg,#5f97cf 0%,#8fb3d4 40%,#dfe4ea 70%,#8b7259 100%)}
  .back-footer{left:0;top:0}
  .back-brand{left:22px;top:840px;color:var(--white);font-size:24px;font-weight:400}
  .back-contact{left:172px;top:812px;color:var(--white);font-size:12.6px;line-height:19px}
  .back-contact .note{font-size:11px;font-weight:300}
  .back-contact .phone{justify-content:flex-start;color:var(--white);font-size:16px}
  .back-socials{left:352px;top:872px;display:flex;gap:6px}
  .back-socials span{width:14px;height:14px;border-radius:2px;background:var(--sky)}
</style>
</head>
<body>

<!-- Front side -->
<section class="card card--front">
  <div class="abs front-photo-top" role="img" aria-label="Photo of the cruising sailboat moored at the marina, cockpit and canopy in view"></div>
  <div class="abs front-photo-main" role="img" aria-label="Photo of the sailboat bow at the dock with the bay and hills behind, under a blue tint"></div>

  <svg class="abs front-shapes" width="433" height="920" viewBox="0 0 433 920">
    <path d="M0 275 Q200 250 433 268 L433 300 Q200 284 0 312 Z" fill="var(--red)"/>
    <path d="M0 300 Q200 280 433 292 L433 300 Q200 290 0 318 Z" fill="var(--blue-deep)"/>
    <path d="M0 820 Q210 780 433 760 L433 800 Q220 815 0 860 Z" fill="var(--red)"/>
    <path d="M0 850 Q220 805 433 790 L433 920 L0 920 Z" fill="var(--white)"/>
  </svg>

  <h1 class="abs front-title">ULTIMATE EAST BAY<br>SAILBOAT CHARTER</h1>

  <svg class="abs badge" width="110" height="110" viewBox="0 0 110 110" role="img" aria-label="Licensed captain credential badge">
    <circle cx="55" cy="55" r="53" fill="var(--white)"/>
    <circle cx="55" cy="55" r="48" fill="var(--blue-dark)"/>
  </svg>

  <ul class="abs checklist">
    <li><svg width="18" height="18" viewBox="0 0 18 18"><rect x="1" y="1" width="16" height="16" fill="none" stroke="#fff" stroke-width="1.6"/><path d="M4 9 L8 13 L14 4" fill="none" stroke="#fff" stroke-width="2"/></svg>MODERN</li>
    <li><svg width="18" height="18" viewBox="0 0 18 18"><rect x="1" y="1" width="16" height="16" fill="none" stroke="#fff" stroke-width="1.6"/><path d="M4 9 L8 13 L14 4" fill="none" stroke="#fff" stroke-width="2"/></svg>ENTERTAINING</li>
    <li><svg width="18" height="18" viewBox="0 0 18 18"><rect x="1" y="1" width="16" height="16" fill="none" stroke="#fff" stroke-width="1.6"/><path d="M4 9 L8 13 L14 4" fill="none" stroke="#fff" stroke-width="2"/></svg>SAFE</li>
  </ul>

  <div class="abs brand-seal">Tidewren</div>

  <div class="abs front-contact">
    <div class="phone">
      <svg width="15" height="15" viewBox="0 0 16 16"><circle cx="8" cy="8" r="7" fill="none" stroke="currentColor" stroke-width="1.4"/><path d="M5.5 4.5 L7 4.5 L7.6 6.6 L6.7 7.3 Q7.5 8.8 8.8 9.4 L9.5 8.5 L11.5 9.1 L11.5 10.6 Q8.5 11.5 6 8.8 Q4.5 6.5 5.5 4.5Z" fill="currentColor"/></svg>
      +1 (510) 555 SAIL (7245)
    </div>
    <div>bookings@SailTidewren.com</div>
    <div>www.sailtidewren.com</div>
    <div class="socials"><span></span><span></span><span></span></div>
  </div>
</section>

<!-- Back side -->
<section class="card card--back">
  <div class="abs intro">
    <h2>WHAT IS WREN?</h2>
    <p>Wren is a 50 foot, center cockpit, cutter rigged, mono-hulled, blue water cruising sail boat. She's a nice sized boat with the driving position and main seats at the center of the boat. She has three positions for sails, main (the big one), jib (front sail) and stay-sail (between main and jib). She has a single hull so will lean over as the wind blows.</p>
  </div>
  <div class="abs intro-rule"></div>
  <div class="abs trip-bg" role="img" aria-label="Faint photo of white sails against the sky"></div>
  <div class="abs trip-tab">THE TRIP</div>

  <div class="abs map" style="left:20px;top:222px" role="img" aria-label="Map of the bay with the two hour route"></div>
  <div class="abs trip" style="left:162px;top:246px;width:250px">
    <h3>2 HOUR BLAST</h3>
    <p>Could be a sunset sail, an early morning wake up cruise or a blast out into the bay anytime to find peace, fresh air and amazing views.</p>
  </div>

  <div class="abs map" style="left:285px;top:357px" role="img" aria-label="Map of the bay with the half day route"></div>
  <div class="abs trip trip--right" style="left:20px;top:370px;width:246px">
    <h3>1/2 DAY FUN</h3>
    <p>Could be a sunset sail, an early morning wake up cruise or a blast out into the bay anytime to find peace, fresh air and amazing views.</p>
  </div>

  <div class="abs map" style="left:20px;top:480px" role="img" aria-label="Map of the bay with the full day circuit route"></div>
  <div class="abs trip" style="left:162px;top:504px;width:250px">
    <h3>FULL DAY ADVENTURE</h3>
    <p style="text-align:justify">The day includes a complete circuit of the Bay and lunch at anchor. Actual duration 7-8 hours</p>
  </div>

  <div class="abs gallery">
    <div class="abs shot" style="left:16px;width:192px" role="img" aria-label="Photo of guests in life jackets in the cockpit"></div>
    <div class="abs shot shot--deck" style="left:223px;width:192px" role="img" aria-label="Photo of the helm and deck looking out over the bay"></div>
  </div>

  <svg class="abs back-footer" width="433" height="920" viewBox="0 0 433 920">
    <path d="M0 765 L433 765 L433 790 Q220 770 0 800 Z" fill="#dfe3ea"/>
    <path d="M0 800 Q220 772 433 790 L433 920 L0 920 Z" fill="var(--blue-deep)"/>
    <path d="M0 800 Q220 772 433 790" fill="none" stroke="var(--white)" stroke-width="2"/>
  </svg>

  <div class="abs back-brand">Tidewren</div>
  <div class="abs back-contact">
    <div class="note">For more detailed information call or click</div>
    <div class="phone">
      <svg width="15" height="15" viewBox="0 0 16 16"><circle cx="8" cy="8" r="7" fill="none" stroke="currentColor" stroke-width="1.4"/><path d="M5.5 4.5 L7 4.5 L7.6 6.6 L6.7 7.3 Q7.5 8.8 8.8 9.4 L9.5 8.5 L11.5 9.1 L11.5 10.6 Q8.5 11.5 6 8.8 Q4.5 6.5 5.5 4.5Z" fill="currentColor"/></svg>
      +1 (510) 555 SAIL (7245)
    </div>
    <div style="margin-top:4px">bookings@SailTidewren.com</div>
    <div>www.sailtidewren.com</div>
  </div>
  <div class="abs back-socials"><span></span><span></span><span></span></div>
</section>

</body>
</html>
```